Redesign www.brightlobco.com

I want a website designer to design my website for me. There is a site up right now but it's not complete because my clients can not pay for my services online. Whoever signs up for this project will have to work on a speedy schedule to be able to complete the new site within a week. I have all of the information online so now at www.brightlobco.com I can send you other files as well. Please let me know if you will be able to do this.

The site needs to be optimize for all platforms like, desktop, laptop, and smartphone.

I do have a quikfund account that we can link to the site to accept transactions.

Thank you,

Rolf

Target Market(s)

Tennis players

Coding

Coded - Design and coding required

Number of Pages Required

5+ page

Font styles to use
Sans Serif
Script

Colors
00a990
a4ce38
ffffff
fbee3f

Requirements
Must have
• Ability to read through the site and ensure that the functionality works. Must have some testing and QA background in order to perform thorough testing and quality assurance prior to delivery. I will prefer a WordPress template for the site.
Nice to have
• Not sure if I will need my own merchant account, but if that's the case, I can get one.

```html
<!DOCTYPE html>
<html lang="en">
<head>
<meta charset="utf-8">
<title>Bright Lob Co. – Tennis Lessons &amp; Camps</title>
<link rel="stylesheet" href="https://fonts.googleapis.com/css2?family=Jost:wght@400;500;600;700&family=Open+Sans:wght@400;600;700&display=swap">
<style>
:root{
  --green:#1b7f3f;
  --green-deep:#136a33;
  --lime:#8dc63f;
  --lime-foot:#9acd45;
  --lime-bar:#7fa83a;
  --clay:#c86a3a;
  --ink:#2b2b2b;
  --muted:#8a8a8a;
  --navy:#2c3d86;
  --grey:#efefef;
  --white:#ffffff;
}
*{box-sizing:border-box;margin:0;padding:0}
html,body{width:1200px;height:3805px;overflow:hidden}
body{font-family:"Open Sans",Arial,sans-serif;color:var(--ink);background:var(--white);position:relative}
section,header,footer{position:absolute;left:0;width:1200px}
.heading{font-family:"Jost",Arial,sans-serif;font-weight:400}

/* header */
.site-header{top:0;height:157px;background:var(--white)}
.nav-bar{position:absolute;top:109px;left:0;width:1200px;height:46px;background:linear-gradient(var(--green),var(--green-deep))}
.brand{position:absolute;left:150px;top:28px;display:flex;align-items:center;gap:14px;z-index:2}
.brand-dot{width:44px;height:44px;border-radius:50%;background:var(--lime)}
.brand-name{font-family:"Jost",sans-serif;font-weight:700;font-size:38px;color:var(--green)}
.phone{position:absolute;right:118px;top:44px;display:flex;align-items:center;gap:10px;font-family:"Jost",sans-serif;font-size:24px;font-weight:500;color:var(--green-deep)}
.nav{position:absolute;right:112px;top:0;height:46px;display:flex;list-style:none}
.nav li{font-family:"Jost",sans-serif;font-size:16px;font-weight:500;color:var(--white);line-height:46px;padding:0 17px;border-left:1px solid rgba(255,255,255,.25)}
.nav li:first-child{border-left:0}

/* hero */
.hero{top:157px;height:523px;background:linear-gradient(100deg,#7a9a7a 0%,#a8c0b0 40%,#d9c7b4 65%,#b49b87 100%)}
.hero-photo{position:absolute;inset:0}
.hero-title{position:absolute;top:180px;width:100%;text-align:center;font-family:"Jost",sans-serif;font-weight:600;font-size:56px;line-height:52px;color:var(--white);letter-spacing:1px}
.dots{position:absolute;display:flex;gap:8px}
.hero .dots{top:488px;left:537px}
.dots span{width:28px;height:5px;background:rgba(255,255,255,.6)}
.dots span.on{background:var(--white)}

/* welcome */
.welcome{top:680px;height:437px;background:var(--white);overflow:hidden}
.welcome-photo{position:absolute;top:0;right:0;width:730px;height:437px;background:linear-gradient(160deg,#6f8f7a 0%,#c9b39c 45%,#c8683a 75%,#b85a30 100%);clip-path:polygon(42% 0,100% 0,100% 100%,0 100%)}
.welcome-body{position:absolute;left:117px;top:74px;width:455px}
.welcome-body h2{font-size:34px;color:#333;margin-bottom:18px}
.welcome-body p{font-size:14px;line-height:23px;color:var(--muted);margin-bottom:14px}
.btn-outline{display:inline-block;margin-top:16px;width:148px;height:40px;border:2px solid var(--navy);color:var(--navy);font-family:"Jost",sans-serif;font-size:13px;font-weight:600;text-align:center;line-height:36px}

/* services */
.services{top:1117px;height:431px;background:var(--grey)}
.section-title{position:absolute;width:100%;text-align:center;font-size:34px;color:#333}
.services .section-title{top:40px}
.service{position:absolute;top:108px;width:330px;height:330px;border-radius:50%;background:var(--white);box-shadow:0 4px 18px rgba(0,0,0,.12);text-align:center;padding:90px 54px 0}
.service.featured{background:var(--lime);color:var(--white);border:6px solid var(--white)}
.service h3{font-family:"Jost",sans-serif;font-weight:500;font-size:22px;margin:10px 0 8px}
.service p{font-size:11.5px;line-height:18px;color:var(--muted)}
.service.featured p{color:var(--white)}
.service svg{display:block;margin:0 auto}

/* camps */
.camps{top:1548px;height:558px;background:linear-gradient(180deg,var(--green) 0%,#1b7a3e 60%,#17703a 100%)}
.camps .curve{position:absolute;top:-40px;left:0}
.camps .section-title{top:110px;color:var(--white)}
.camp-row{position:absolute;left:117px;top:190px;display:flex;gap:5px}
.camp{position:relative;width:238px;height:297px}
.camp-photo{position:absolute;inset:0}
.camp-label{position:absolute;left:0;bottom:0;width:100%;height:48px;background:rgba(141,198,63,.88);color:var(--white);font-family:"Jost",sans-serif;font-size:17px;font-weight:500;line-height:48px;padding:0 16px;display:flex;justify-content:space-between;align-items:center}

/* training */
.training{top:2106px;height:444px;background:var(--clay)}
.training-photo{position:absolute;left:0;top:0;width:630px;height:444px;background:linear-gradient(120deg,#c26234 0%,#d98a55 45%,#c86a3a 100%)}
.training-body{position:absolute;left:657px;top:96px;width:500px;color:var(--white)}
.training-body h2{font-size:34px;margin-bottom:14px}
.training-body p{font-size:13px;line-height:22px}
.btn-lime{display:inline-block;margin-top:22px;width:147px;height:36px;background:var(--lime);color:var(--white);font-family:"Jost",sans-serif;font-size:13px;font-weight:600;text-align:center;line-height:36px}

/* coaches */
.coaches{top:2550px;height:393px;background:var(--white)}
.coaches .section-title{top:56px}
.coach{position:absolute;top:144px;display:flex;gap:17px}
.coach-photo{width:137px;height:125px;flex:none}
.coach h4{font-family:"Jost",sans-serif;font-weight:500;font-size:17px;color:var(--lime);margin-bottom:4px}
.coach p{font-size:11.5px;line-height:17px;color:var(--muted);width:120px}
.coach a{display:block;margin-top:6px;font-size:11.5px;font-weight:600;color:var(--green);text-decoration:none}
.coaches .dots{top:322px;left:553px}
.coaches .dots span{width:30px;height:4px;background:#d0d0d0}
.coaches .dots span.on{background:var(--lime)}

/* testimonial */
.testimonial{top:2943px;height:419px;background:linear-gradient(90deg,#e2e6e2,#f1f1f1 30%,#f1f1f1 70%,#e2e6e2)}
.testimonial .section-title{top:50px;color:var(--navy);font-size:30px}
.quote-card{position:absolute;left:310px;top:140px;width:634px;height:215px;background:var(--white);border-radius:108px;box-shadow:0 4px 16px rgba(0,0,0,.08)}
.quote-mark{position:absolute;left:600px;top:120px;width:56px;height:56px;border-radius:50%;background:var(--lime);z-index:2;display:flex;align-items:center;justify-content:center;color:var(--white);font-family:"Jost",sans-serif;font-size:44px;font-weight:700;line-height:1;padding-top:18px}
.avatar{position:absolute;left:70px;top:45px;width:90px;height:90px;border-radius:50%;background:linear-gradient(#c9a98a,#8a6b52)}
.quote-text{position:absolute;left:177px;top:44px;width:400px;font-size:13px;line-height:22px;font-style:italic;color:var(--muted)}
.quote-author{position:absolute;left:183px;top:150px;font-size:15px;font-weight:600;color:#333}
.arrow{position:absolute;top:150px}

/* footer */
.site-footer{top:3362px;height:368px;background:var(--lime-foot);color:var(--white)}
.col{position:absolute;top:72px}
.col h5{font-family:"Jost",sans-serif;font-weight:500;font-size:19px;margin-bottom:14px}
.col li{list-style:none;font-size:13.5px;line-height:30px}
.contact li{display:flex;gap:12px;align-items:flex-start;line-height:24px;margin-bottom:6px;width:320px}
.contact svg{flex:none;margin-top:5px}
.socials{display:flex;gap:6px;margin-top:8px}
.socials span{width:24px;height:24px;border-radius:50%;border:1.5px solid var(--white)}
.bottom-bar{position:absolute;top:3730px;left:0;width:1200px;height:75px;background:var(--lime-bar);color:rgba(255,255,255,.85);font-size:12px;text-align:center;line-height:75px}
</style>
</head>
<body>

<header class="site-header">
  <div class="nav-bar">
    <ul class="nav">
      <li>HOME</li><li>ABOUT</li><li>SUMMER CAMP</li><li>OUR SERVICES</li><li>BLOG</li><li>BOOK LESSON</li><li>CONTACT</li>
    </ul>
  </div>
  <div class="brand"><span class="brand-dot"></span><span class="brand-name">Bright Lob Co.</span></div>
  <div class="phone">
    <svg width="20" height="20" viewBox="0 0 24 24"><path fill="#1b7f3f" d="M6.6 10.8a15 15 0 0 0 6.6 6.6l2.2-2.2c.3-.3.7-.4 1-.2 1.1.4 2.3.6 3.6.6.6 0 1 .4 1 1V20c0 .6-.4 1-1 1A17 17 0 0 1 3 4c0-.6.4-1 1-1h3.5c.6 0 1 .4 1 1 0 1.3.2 2.5.6 3.6.1.3 0 .7-.2 1z"/></svg>
    555-210-4870
  </div>
</header>

<section class="hero">
  <div class="hero-photo" role="img" aria-label="Photo of a smiling woman holding a tennis racket on an outdoor court"></div>
  <h1 class="hero-title">THE MORE YOU SWEAT<br>IN TRAINING</h1>
  <div class="dots"><span class="on"></span><span></span><span></span><span></span></div>
</section>

<section class="welcome">
  <div class="welcome-photo" role="img" aria-label="Photo of a coach teaching a young girl tennis at the net on a clay court"></div>
  <div class="welcome-body">
    <h2 class="heading">Welcome to Our Webstie</h2>
    <p>Fusce ultricies orci ac feugiat suscipit leo massa sodales velit et scelerisque mi tortor at ipsum cligula augue bibendum accumsan vestibulum ut commodo a mi Morbi ornare gravida elit integer congue augue et malesuada</p>
    <p>Iaculis quis dolor ut aliquet felis at cursus magna nisl nec elit Praesent elementum elit at tellus nec ultricies sit</p>
    <span class="btn-outline">LEARN MORE</span>
  </div>
</section>

<section class="services">
  <h2 class="section-title heading">Our Services</h2>
  <div class="service" style="left:127px">
    <svg width="40" height="40" viewBox="0 0 40 40" fill="none" stroke="#1b7f3f" stroke-width="2.2"><ellipse cx="25" cy="14" rx="9" ry="10" transform="rotate(40 25 14)"/><path d="M18 21 7 33"/><circle cx="9" cy="9" r="4"/></svg>
    <h3>Tennis Lessons</h3>
    <p>Class aptent taciti sociosqu ad litora torquent per conubia nostra per inceptos hymenaeos Proin nulla arcu</p>
  </div>
  <div class="service featured" style="left:431px;top:102px;width:340px;height:340px">
    <svg width="48" height="40" viewBox="0 0 48 40" fill="none" stroke="#fff" stroke-width="2.2"><path d="M10 12h28l6 18H4z"/><path d="M4 30v4h40v-4M24 12v18M7 21h34"/></svg>
    <h3>Tennis Drills</h3>
    <p>Class aptent taciti sociosqu ad litora torquent per conubia nostra per inceptos hymenaeos Proin nulla arcu</p>
  </div>
  <div class="service" style="left:753px">
    <svg width="44" height="40" viewBox="0 0 44 40" fill="none" stroke="#1b7f3f" stroke-width="2.2"><path d="M3 8h24v22H3zM27 16h8l6 7v7H27"/><circle cx="10" cy="32" r="3.5"/><circle cx="34" cy="32" r="3.5"/><path d="m9 19 4 4 7-8"/></svg>
    <h3>Transporation Service</h3>
    <p>Class aptent taciti sociosqu ad litora torquent per conubia nostra per inceptos hymenaeos Proin nulla arcu</p>
  </div>
</section>

<section class="camps">
  <svg class="curve" width="1200" height="90" viewBox="0 0 1200 90"><path d="M0 40 Q600 -10 1200 40 V90 H0z" fill="#d8ecd0"/><path d="M0 50 Q600 0 1200 50 V90 H0z" fill="#1b7f3f"/></svg>
  <h2 class="section-title heading">Summer Camps</h2>
  <div class="camp-row">
    <div class="camp"><div class="camp-photo" role="img" aria-label="Photo of two smiling kids holding tennis rackets" style="background:linear-gradient(#d96a3a,#a94a2a)"></div><div class="camp-label">Camp Title here <span>›</span></div></div>
    <div class="camp"><div class="camp-photo" role="img" aria-label="Photo of a child hitting a ball on a tennis court" style="background:linear-gradient(#5d8a5a,#c06a45)"></div><div class="camp-label">Camp Title here <span>›</span></div></div>
    <div class="camp"><div class="camp-photo" role="img" aria-label="Photo of a group of children holding tennis balls" style="background:linear-gradient(#8fb0d8,#6b9a4a)"></div><div class="camp-label">Camp Title here <span>›</span></div></div>
    <div class="camp"><div class="camp-photo" role="img" aria-label="Photo of young players with rackets on court" style="background:linear-gradient(#c98f70,#7a8f6a)"></div><div class="camp-label">Camp Title here <span>›</span></div></div>
  </div>
</section>

<section class="training">
  <div class="training-photo" role="img" aria-label="Photo of a coach tossing a ball to a boy with a racket on a clay court"></div>
  <div class="training-body">
    <h2 class="heading">Our Training</h2>
    <p>aliquam Curabitur iaculis tempus eros Curabitur vel mi sit amet magna malesuada ultrices Ut nisl erat fermentum vel congue id euismod in elit Fusce ultricies orci ac feugiat suscipit leo massa sodales velit et scelerisque mi tortor at ipsum cligula augue bibendum accumsan Morbi ornare gravida elit</p>
    <span class="btn-lime">LEARN MORE</span>
  </div>
</section>

<section class="coaches">
  <h2 class="section-title heading">Our Coaches</h2>
  <div class="coach" style="left:117px"><div class="coach-photo" role="img" aria-label="Portrait of a coach" style="background:linear-gradient(#7fb0a0,#4a7d8a)"></div><div><h4>Coach Name</h4><p>conubia nostra per inceptos hymenaeos Proin nulla arcu nonummy luctus</p><a>Read More</a></div></div>
  <div class="coach" style="left:444px"><div class="coach-photo" role="img" aria-label="Portrait of a coach in an orange shirt" style="background:linear-gradient(#8a7a6a,#d0622a)"></div><div><h4>Coach Name</h4><p>conubia nostra per inceptos hymenaeos Proin nulla arcu nonummy luctus</p><a>Read More</a></div></div>
  <div class="coach" style="left:776px"><div class="coach-photo" role="img" aria-label="Portrait of a young player with a tennis ball" style="background:linear-gradient(#6a9a4a,#9a3a4a)"></div><div><h4>Coach Name</h4><p>conubia nostra per inceptos hymenaeos Proin nulla arcu nonummy luctus</p><a>Read More</a></div></div>
  <div class="dots"><span></span><span class="on"></span><span></span></div>
</section>

<section class="testimonial">
  <h2 class="section-title heading">What Our Client Says</h2>
  <div class="quote-mark">“</div>
  <svg class="arrow" style="left:252px" width="30" height="60" viewBox="0 0 30 60"><path d="M24 4 6 30l18 26" fill="none" stroke="#333" stroke-width="2.5"/></svg>
  <svg class="arrow" style="left:960px" width="30" height="60" viewBox="0 0 30 60"><path d="m6 4 18 26L6 56" fill="none" stroke="#333" stroke-width="2.5"/></svg>
  <div class="quote-card">
    <div class="avatar" role="img" aria-label="Client portrait"></div>
    <p class="quote-text">You've taken everyone's kids a very long way on this road to success and their lives are much the better for it. They showed everyone what the results of working with a stellar coach look like. Many, many thanks to you Rolf.</p>
    <p class="quote-author">By Author Name</p>
  </div>
</section>

<footer class="site-footer">
  <div class="col" style="left:167px"><h5>Company</h5><ul><li>About Us</li><li>Our Team</li><li>Testimonials</li></ul><div class="socials"><span></span><span></span><span></span><span></span></div></div>
  <div class="col" style="left:373px"><h5>Sublinks</h5><ul><li>Summer Camps</li><li>Our Services</li><li>Coaches</li><li>Training</li></ul></div>
  <div class="col" style="left:601px"><h5>Resources</h5><ul><li>Blogs</li><li>Gallery</li><li>Contact</li></ul></div>
  <div class="col contact" style="left:817px"><h5>Contact Us</h5>
    <ul>
      <li><svg width="14" height="16" viewBox="0 0 14 18"><path fill="#fff" d="M7 0a7 7 0 0 0-7 7c0 5 7 11 7 11s7-6 7-11a7 7 0 0 0-7-7zm0 9.5A2.5 2.5 0 1 1 7 4.5a2.5 2.5 0 0 1 0 5z"/></svg>Bright Lob Co. Courts Suite 12, 48 Baseline Avenue, Fairview, VA 22030</li>
      <li><svg width="14" height="14" viewBox="0 0 24 24"><path fill="#fff" d="M6.6 10.8a15 15 0 0 0 6.6 6.6l2.2-2.2c.3-.3.7-.4 1-.2 1.1.4 2.3.6 3.6.6.6 0 1 .4 1 1V20c0 .6-.4 1-1 1A17 17 0 0 1 3 4c0-.6.4-1 1-1h3.5c.6 0 1 .4 1 1 0 1.3.2 2.5.6 3.6.1.3 0 .7-.2 1z"/></svg>+1 555 210 4871</li>
      <li><svg width="15" height="12" viewBox="0 0 20 14"><path fill="#fff" d="M0 0h20v14H0z"/><path d="m1 1 9 7 9-7" fill="none" stroke="#9acd45" stroke-width="1.6"/></svg>hello@brightlobco.com</li>
    </ul>
  </div>
</footer>
<div class="bottom-bar">© 2017 Company Name. All right reserved. Term of Use</div>

</body>
</html>
```